I am looking for a layout for signs and banners. Red being the prominent color and using blue and white in it. I am looking for sleek and clean not busy look. I would like to see some with the the US flag in the art work or in the background as well. I need a catchy visual logo for this political campaign. The banners and signs need to have Dena Holcroft for US Congress.

At the bottom of all it should say "paid for by the Dena Holcroft for US Congress"

```html
<!DOCTYPE html>
<html lang="en">
<head>
<meta charset="utf-8">
<title>Dena Holcroft for US Congress</title>
<link rel="stylesheet" href="https://fonts.googleapis.com/css2?family=ABeeZee&display=swap">
<style>
  :root {
    --campaign-red: #c2001a;
    --headline-white: #ffffff;
    --office-blue: #a9cdf2;
    --disclaimer-pink: #f49ac1;
    --flag-blue: #1f2fd6;
    --flag-white: #f4f4f8;
    --flag-red: #d0102a;
  }
  html, body {
    margin: 0;
    padding: 0;
    overflow: hidden;
    background: var(--campaign-red);
  }
  .campaign-sign {
    position: relative;
    width: 1200px;
    height: 1200px;
    background: var(--campaign-red);
    font-family: "ABeeZee", sans-serif;
    overflow: hidden;
  }
  .candidate-name {
    position: absolute;
    top: 108px;
    left: 0;
    width: 100%;
    margin: 0;
    text-align: center;
    font-size: 90px;
    font-weight: 400;
    line-height: 1;
    letter-spacing: 0.01em;
    color: var(--headline-white);
    text-transform: uppercase;
  }
  .office-sought {
    position: absolute;
    top: 202px;
    left: 0;
    width: 100%;
    margin: 0;
    text-align: center;
    font-size: 42px;
    line-height: 1;
    letter-spacing: 0.14em;
    color: var(--office-blue);
    text-transform: uppercase;
  }
  .flag-map {
    position: absolute;
    left: 233px;
    top: 424px;
    width: 736px;
    height: 387px;
  }
  .paid-for-by {
    position: absolute;
    top: 1014px;
    left: 0;
    width: 100%;
    margin: 0;
    text-align: center;
    font-size: 44px;
    line-height: 1;
    color: var(--disclaimer-pink);
  }
</style>
</head>
<body>
  <main class="campaign-sign">
    <h1 class="candidate-name">Dena Holcroft</h1>
    <p class="office-sought">For US Congress</p>

    <svg class="flag-map" viewBox="0 0 736 387" role="img" aria-label="Map of the United States filled with the American flag, blue star field at upper left and red and white stripes">
      <defs>
        <radialGradient id="starFieldTone" cx="0.2" cy="0.28" r="0.45">
          <stop offset="0" stop-color="var(--flag-blue)"/>
          <stop offset="0.55" stop-color="var(--flag-blue)" stop-opacity="0.85"/>
          <stop offset="1" stop-color="var(--flag-blue)" stop-opacity="0"/>
        </radialGradient>
        <linearGradient id="stripeTone" x1="0" y1="0" x2="1" y2="1">
          <stop offset="0" stop-color="var(--flag-white)"/>
          <stop offset="0.6" stop-color="#f1d4d9"/>
          <stop offset="1" stop-color="var(--flag-red)" stop-opacity="0.75"/>
        </linearGradient>
      </defs>
      <rect x="0" y="0" width="736" height="387" rx="40" fill="url(#stripeTone)"/>
      <rect x="0" y="0" width="736" height="387" rx="40" fill="url(#starFieldTone)"/>
    </svg>

    <p class="paid-for-by">Paid for by the Dena Holcroft for US Congress</p>
  </main>
</body>
</html>
```